International game business needs app design

We are planning to release a new mobile game on Qbe5 which requires a fresh, flat, reduced and functional design, fulfilling Brindle’s Qbe5 design guidelines
.
The design shall be created for a dashboard, where players should be able to pick levels (icon + short description; 300+ levels), opponents (icon/photo/avatar image + short description; 5-100) and read/delete system/chat messages (icon, 2-3 actions (delete, accept/decline), text with up to 500 characters; 1-100 entries), Menu bar (settings, shop, leaderboards, achievements, and one or two more menu items) It must consider means to search/select levels and opponents. Would be nice to have an option to start playing immediately (with a random opponent on a random level)

Overall Style/Look: fresh, flat, functional, lot’s of free space, warm color scheme. If full screen images are being used it must be considered that there are user-generated photos or avatars which have to work with it in combination

Ideally the design is responsive and would work both on a smartphone and a tablet. Smartphone is top priority, tablet is optional.

The app will be a game for women predominantly, aged 25-35, with higher education and household net income, which should be reflected in color scheme, icons and navigation.

Some of us like flat design, so you might stick to that or impress all of us with something completely new!

The winner will have the chance to design all screens for the app and will have access to a much bigger budget.

UPDATE: A wireframe is attached - but you don't have to follow the depicted layout. Actually it would be highly appreciated if you could come up with something new. The only important thing is that all the listed components must appear somehow on the dashboard.

Target Market(s)

US, AU, NZ, GB, CA

Industry/Entity Type

Education

Colors

Designer to choose colors to be used in the design.

Requirements
Must have
• All the functional components described above.
Design must be in line with Qbe5 design guidelines https://makers.brindlehub.example/library/qbe/documentation/UserExperience/Conceptual/TouchGuide/index.html
Nice to have
• We would like to have someone with the following attributes:
* minimum 5 qbe design in your past at least 2 of them responsive – please provide links to the apps you created
* besides UI designer skills would be nice you to have UX skills

The most important factors for us are quality, creativity, speed, flexibility (“be able to take criticism into account”)
Should not have
• We don’t want a girly design so please don’t use too much pinks, flowers and such. The design should be acceptable by men too.

```html
<!DOCTYPE html>
<html lang="en">
<head>
<meta charset="utf-8">
<title>Level Dashboard</title>
<link rel="stylesheet" href="https://fonts.googleapis.com/css2?family=Roboto:ital,wght@0,300;0,400;0,500;0,700;1,300;1,400&family=Roboto+Condensed:wght@400;700&display=swap">
<style>
:root{
  --stage:#4a3a22;
  --sun:#ffd500;
  --amber:#ffa200;
  --tangerine:#ff7a00;
  --ember:#e35300;
  --ink:#111111;
  --paper:#ffffff;
  --mute:#8a8a8a;
  --lime:#7ee000;
  --band:rgba(120,70,0,.45);
}
*{box-sizing:border-box;margin:0;padding:0}
html,body{width:1117px;height:1200px;overflow:hidden}
body{background:var(--stage);font-family:"Roboto",Arial,sans-serif;position:relative}
.screen{position:absolute;left:238px;top:32px;width:640px;height:1136px;overflow:hidden;
  background:linear-gradient(120deg,var(--sun) 0%,var(--amber) 45%,var(--tangerine) 100%)}
.status-bar{position:absolute;top:0;left:0;right:0;height:40px;color:var(--paper);font-size:25px;display:flex;align-items:center;padding:0 14px}
.status-bar .carrier{display:flex;align-items:center;gap:5px}
.status-bar .dots{display:flex;gap:3px;margin-right:4px}
.status-bar .dots i{width:10px;height:10px;border-radius:50%;background:var(--paper)}
.status-bar .dots i.empty{background:none;border:1.5px solid var(--paper)}
.status-bar .right{margin-left:auto;display:flex;align-items:center;gap:8px}
.battery{width:44px;height:20px;border:2px solid var(--paper);border-radius:4px;padding:2px}
.battery span{display:block;width:82%;height:100%;background:var(--paper)}

.level-strip{position:absolute;top:78px;left:0;width:640px;height:230px}
.level-card{position:absolute;top:16px;width:154px;height:186px;border:2px solid rgba(255,255,255,.85);border-radius:6px;color:var(--paper);text-align:center}
.level-card .tab{position:absolute;top:-18px;left:50%;margin-left:-31px}
.level-card h3{font-weight:300;font-size:29px;margin-top:36px;letter-spacing:-.3px}
.level-card p{font-size:11px;line-height:14px;margin:10px 16px 0}
.level-card.is-current{background:var(--paper);color:var(--ember);border-color:var(--paper)}
.level-card.is-current p{color:#333}
.level-card .add{position:absolute;bottom:-14px;left:50%;margin-left:-13px}

.opponent-band{position:absolute;top:316px;left:0;width:640px;height:208px;background:linear-gradient(90deg,var(--band),rgba(200,70,0,.25))}
.opponent-band text{font-family:"Roboto Condensed","Arial Narrow",sans-serif}

.play-bar{position:absolute;top:528px;left:28px;width:596px;height:76px}
.play-bar .pill{position:absolute;top:12px;left:0;width:540px;height:60px;background:var(--ink);border-radius:6px;color:var(--paper);font-weight:300;font-size:26px;display:flex;align-items:center;padding-left:38px;letter-spacing:.3px}
.play-bar .pill b{color:var(--tangerine);font-weight:500}
.play-bar .go{position:absolute;left:506px;top:0}

.chat-feed{position:absolute;top:612px;left:0;width:640px;height:424px}
.bubble{position:absolute;background:var(--paper);border-radius:6px;height:84px}
.bubble::after{content:"";position:absolute;bottom:-12px;width:0;height:0;border-top:12px solid var(--paper);border-left:10px solid transparent;border-right:10px solid transparent}
.bubble.tail-right::after{right:24px}
.bubble .author{font-size:11px;color:var(--mute)}
.bubble .author em{font-style:normal;color:var(--tangerine)}
.bubble .message{font-size:21px;font-style:italic;font-weight:300;color:var(--mute);margin-top:4px}
.bubble .message em{color:var(--tangerine);font-weight:400}
.bubble .text{position:absolute;top:14px}
.avatar-hex{position:absolute}
.badge-hex{position:absolute}
.scroll-track{position:absolute;right:10px;top:14px;width:3px;height:150px;background:rgba(60,20,0,.6);border-radius:2px}
.bubble.faded{opacity:.35;height:40px}

.tab-bar{position:absolute;left:0;top:1036px;width:640px;height:100px;background:var(--paper)}
.tab-bar .rail{position:absolute;left:0;right:0;top:49px;height:3px;background:var(--ink)}
.tab-bar svg{position:absolute}
</style>
</head>
<body>
<main class="screen">
  <header class="status-bar">
    <div class="carrier"><span class="dots"><i></i><i></i><i></i><i></i><i class="empty"></i></span>LUMEN
      <svg width="26" height="20" viewBox="0 0 26 20"><path d="M1 7a17 17 0 0 1 24 0M5 11a11 11 0 0 1 16 0M9 15a5 5 0 0 1 8 0" fill="none" stroke="#fff" stroke-width="2.6" stroke-linecap="round"/></svg>
    </div>
    <div class="right">
      <svg width="12" height="22" viewBox="0 0 12 22"><path d="M1 6l10 9-5 5V2l5 5-10 9" fill="none" stroke="#fff" stroke-width="1.6"/></svg>
      <span>82%</span>
      <div class="battery"><span></span></div>
      <svg width="10" height="18" viewBox="0 0 10 18"><path d="M6 0L0 10h4l-1 8 7-11H6z" fill="#fff"/></svg>
    </div>
  </header>

  <section class="level-strip" aria-label="Levels">
    <article class="level-card" style="left:20px">
      <svg class="tab" width="62" height="46" viewBox="0 0 62 46"><polygon points="2,23 16,2 46,2 60,23 46,44 16,44" fill="var(--amber)" stroke="#fff" stroke-width="2"/></svg>
      <h3>Level 293</h3>
      <p>Tidy the pantry and stack the jars by colour before lunch</p>
    </article>
    <article class="level-card is-current" style="left:192px">
      <svg class="tab" width="62" height="46" viewBox="0 0 62 46"><polygon points="2,23 16,2 46,2 60,23 46,44 16,44" fill="var(--amber)" stroke="#fff" stroke-width="2"/></svg>
      <h3>Level 294</h3>
      <p>Find the hidden keys in the garden room</p>
      <svg class="add" width="26" height="26" viewBox="0 0 26 26"><circle cx="13" cy="13" r="11" fill="var(--amber)" stroke="#fff" stroke-width="2"/><path d="M13 7v12M7 13h12" stroke="#fff" stroke-width="2"/></svg>
    </article>
    <article class="level-card" style="left:364px">
      <svg class="tab" width="62" height="46" viewBox="0 0 62 46"><polygon points="2,23 16,2 46,2 60,23 46,44 16,44" fill="var(--tangerine)" stroke="#fff" stroke-width="2"/></svg>
      <h3>Level 295</h3>
      <p>Match the teacups, then set the table for six</p>
    </article>
    <article class="level-card" style="left:536px">
      <svg class="tab" width="62" height="46" viewBox="0 0 62 46"><polygon points="2,23 16,2 46,2 60,23 46,44 16,44" fill="var(--tangerine)" stroke="#fff" stroke-width="2"/></svg>
      <h3>Level 296</h3>
      <p>Sort the letters by date and file them away neatly</p>
    </article>
  </section>

  <section class="opponent-band" aria-label="Opponents">
    <svg width="640" height="208" viewBox="0 0 640 208">
      <defs>
        <linearGradient id="avatarTone" x1="0" y1="0" x2="0" y2="1"><stop offset="0" stop-color="#6b4a3a"/><stop offset="1" stop-color="#c9a08a"/></linearGradient>
      </defs>
      <g fill="none" stroke="#fff" stroke-width="2">
        <polygon points="0,80 29,18 87,18 116,80 87,142 29,142"/>
        <polygon points="110,148 139,88 197,88 226,148 197,208 139,208"/>
        <polygon points="222,80 251,18 309,18 338,80 309,142 251,142"/>
        <polygon points="332,148 361,88 419,88 448,148 419,208 361,208"/>
        <polygon points="446,80 475,18 533,18 562,80 533,142 475,142" fill="#fff"/>
        <polygon points="556,148 585,88 643,88 672,148 643,208 585,208"/>
      </g>
      <g fill="#fff" text-anchor="middle">
        <text x="58" y="48" font-size="15">Lena</text><text x="58" y="64" font-size="15">Marsh</text>
        <text x="58" y="94" font-size="18">1 540 pt</text>
        <text x="168" y="140" font-size="18">9 930 pt</text><text x="168" y="170" font-size="15">Ivy Hale</text>
        <text x="280" y="48" font-size="15">Clara</text><text x="280" y="64" font-size="15">Vance</text>
        <text x="280" y="94" font-size="18">21 930 pt</text>
        <text x="390" y="140" font-size="18">390 pt</text><text x="390" y="170" font-size="15">Esme Rowe</text>
        <text x="614" y="140" font-size="18">7 230 pt</text><text x="600" y="166" font-size="15">Tessa</text><text x="600" y="182" font-size="15">Lund</text>
      </g>
      <text x="504" y="60" font-size="15" fill="var(--ember)" text-anchor="middle">Nora Kell</text>
      <text x="504" y="94" font-size="18" fill="#222" text-anchor="middle">192 382 pt</text>
      <circle cx="504" cy="18" r="11" fill="var(--ember)" stroke="#fff" stroke-width="2"/><path d="M504 12v12M498 18h12" stroke="#fff" stroke-width="2"/>
      <g stroke="#fff" stroke-width="1.5" fill="url(#avatarTone)">
        <polygon role="img" aria-label="Player avatar" points="44,124 51,112 65,112 72,124 65,136 51,136"/>
        <polygon role="img" aria-label="Player avatar" points="154,96 161,84 175,84 182,96 175,108 161,108"/>
        <polygon role="img" aria-label="Player avatar" points="266,124 273,112 287,112 294,124 287,136 273,136"/>
        <polygon role="img" aria-label="Player avatar" points="376,96 383,84 397,84 404,96 397,108 383,108"/>
        <polygon role="img" aria-label="Player avatar" points="490,124 497,112 511,112 518,124 511,136 497,136"/>
        <polygon role="img" aria-label="Player avatar" points="600,96 607,84 621,84 628,96 621,108 607,108"/>
      </g>
    </svg>
  </section>

  <section class="play-bar">
    <div class="pill">PLAY LEVEL&nbsp;<b>294</b>&nbsp;WITH&nbsp;<b>NORA KELL</b></div>
    <svg class="go" width="90" height="84" viewBox="0 0 90 84"><polygon points="3,42 24,5 66,5 87,42 66,79 24,79" fill="var(--lime)" stroke="#fff" stroke-width="3"/><path d="M28 42h32M48 30l12 12-12 12" fill="none" stroke="#111" stroke-width="3" stroke-linecap="round" stroke-linejoin="round"/></svg>
  </section>

  <section class="chat-feed" aria-label="Messages">
    <div class="scroll-track"></div>
    <article class="bubble tail-right" style="left:14px;top:14px;width:600px;height:80px">
      <div class="text" style="left:146px"><div class="author"><em>Clara Vance</em> wrote:</div><div class="message">Hey, whats up?</div></div>
    </article>
    <svg class="avatar-hex" style="left:20px;top:4px" width="126" height="100" viewBox="0 0 126 100"><polygon role="img" aria-label="Player portrait" points="3,50 30,3 96,3 123,50 96,97 30,97" fill="url(#chatTone)" stroke="#fff" stroke-width="3"/><defs><linearGradient id="chatTone" x1="0" y1="0" x2="1" y2="1"><stop offset="0" stop-color="#7a3a20"/><stop offset="1" stop-color="#d9a487"/></linearGradient></defs></svg>

    <article class="bubble tail-right" style="left:14px;top:124px;width:600px;height:90px">
      <svg class="badge-hex" style="left:18px;top:22px" width="60" height="50" viewBox="0 0 60 50"><polygon points="2,25 15,2 45,2 58,25 45,48 15,48" fill="#fff" stroke="#ddd" stroke-width="2"/><text x="30" y="32" text-anchor="middle" font-size="19" font-style="italic" fill="var(--tangerine)" font-family="Roboto,sans-serif">429</text></svg>
      <div class="text" style="left:102px;top:20px"><div class="author"><em>Nora Kell</em> wrote:</div><div class="message">Hey, let's play level 429</div></div>
    </article>
    <svg class="avatar-hex" style="left:490px;top:118px" width="126" height="102" viewBox="0 0 126 102"><polygon role="img" aria-label="Player portrait" points="3,51 30,3 96,3 123,51 96,99 30,99" fill="url(#chatTone)" stroke="#fff" stroke-width="3"/></svg>

    <article class="bubble tail-right" style="left:14px;top:254px;width:600px;height:88px">
      <div class="text" style="left:146px;top:18px"><div class="message" style="margin:0"><em>Clara Vance</em> just played level 3.</div><div class="message">Why don't you play this too?</div></div>
      <svg class="badge-hex" style="left:512px;top:20px" width="60" height="50" viewBox="0 0 60 50"><polygon points="2,25 15,2 45,2 58,25 45,48 15,48" fill="#fff" stroke="#ddd" stroke-width="2"/><text x="30" y="32" text-anchor="middle" font-size="19" font-style="italic" fill="var(--tangerine)" font-family="Roboto,sans-serif">3</text></svg>
    </article>
    <svg class="avatar-hex" style="left:20px;top:244px" width="126" height="108" viewBox="0 0 126 108"><polygon role="img" aria-label="Player portrait" points="3,54 30,3 96,3 123,54 96,105 30,105" fill="#3a2a22" stroke="#fff" stroke-width="3"/><path d="M63 36l20 34H43z" fill="none" stroke="#fff" stroke-width="3" stroke-linejoin="round"/><path d="M63 48v10M63 62v3" stroke="#fff" stroke-width="3"/></svg>

    <article class="bubble faded" style="left:14px;top:384px;width:600px"></article>
  </section>

  <nav class="tab-bar" aria-label="Menu">
    <div class="rail"></div>
    <svg style="left:24px;top:12px" width="92" height="76" viewBox="0 0 92 76"><polygon points="2,38 22,2 70,2 90,38 70,74 22,74" fill="#111"/><g stroke="#fff" stroke-width="3" stroke-linecap="round"><path d="M36 24v28M46 24v28M56 24v28"/><path d="M32 32h8M42 44h8M52 30h8"/></g></svg>
    <svg style="left:124px;top:12px" width="92" height="76" viewBox="0 0 92 76"><polygon points="2,38 22,2 70,2 90,38 70,74 22,74" fill="#111"/><path d="M36 24h20v8a10 10 0 0 1-20 0zM36 27h-5a6 6 0 0 0 6 8M56 27h5a6 6 0 0 1-6 8M46 42v8M39 52h14" fill="none" stroke="#fff" stroke-width="3" stroke-linejoin="round"/></svg>
    <svg style="left:224px;top:12px" width="92" height="76" viewBox="0 0 92 76"><polygon points="2,38 22,2 70,2 90,38 70,74 22,74" fill="#111"/><path d="M28 26h6l5 18h18l4-13H36" fill="none" stroke="#fff" stroke-width="3" stroke-linejoin="round"/><circle cx="41" cy="51" r="3" fill="#fff"/><circle cx="55" cy="51" r="3" fill="#fff"/></svg>
    <svg style="left:324px;top:12px" width="92" height="76" viewBox="0 0 92 76"><polygon points="2,38 22,2 70,2 90,38 70,74 22,74" fill="#111"/><path d="M40 20h12v10H40z" fill="#fff"/><circle cx="46" cy="42" r="11" fill="none" stroke="#fff" stroke-width="3"/><path d="M46 36l2 4h4l-3 3 1 4-4-2-4 2 1-4-3-3h4z" fill="#fff"/></svg>
    <svg style="left:424px;top:12px" width="92" height="76" viewBox="0 0 92 76"><polygon points="2,38 22,2 70,2 90,38 70,74 22,74" fill="#111"/><circle cx="44" cy="36" r="10" fill="none" stroke="#fff" stroke-width="3"/><path d="M51 43l8 8" stroke="#fff" stroke-width="4" stroke-linecap="round"/></svg>
    <svg style="left:528px;top:6px" width="104" height="88" viewBox="0 0 104 88"><polygon points="2,44 25,2 79,2 102,44 79,86 25,86" fill="var(--tangerine)" stroke="#111" stroke-width="2.5"/><g fill="none" stroke="#fff" stroke-width="3" stroke-linecap="round" stroke-linejoin="round"><path d="M32 34h10l18 20h10M32 54h10l5-6M55 40l5-6h10"/><path d="M66 30l4 4-4 4M66 50l4 4-4 4"/></g></svg>
  </nav>
</main>
</body>
</html>
```